QLV Fashion Design Company Needs a New Web Design, Please Click Me

Designers:

PLEASE NOTE: we only need the web page design, not a fully coded website.

Our brand's name is The Bright Quarry, our signature is print. our style is edgy and chic.

The old website is too messy. here's the address:
www.qlvstudio.com.cn

The new website's purpose is to show our brand/design and most importantly, sell products, So it should be a combination of a designer official website and online shopping. I want the whole style to be clean, edgy and pioneer, easy to understand. we need a sophisticated online shopping website.

The reference websites are:
merolatest.co.uk
www.pd-kor.com
lucasvemm.com
orbaduvi.com
talumerosapkin.com

Please beat their designs :)

Check out our lasted fashion show to get to know us more.

https://www.vidplexa.com/watch?v=ZkamWtrBnoLe&spfreload=10

The attachments are our Logo and some 2015 Look Book.
(Please let us know if you want to play with our print in this particular web design, we can send the source file.)
Updates

Designers, we really like the design of ameliadrovenko.com(we have attached a picture of the website) , Can we get a homepage like that? so the designs you submit will be 3 pages. The first one should be a page that only has Shop/Look. then the shop page, it should be nothing but our product which we will list the categories ourself. And the look page should contain all the info. such as news, about us and designers etc. Thank you all for your hard work, we really enjoyed the designs. Added Monday, November 03, 2014

Target Market(s)

Our target audiences are woman aged from 16-40 who like online shopping

Industry/Entity Type

Online Shopping

Number of Pages Required

3 page

Font styles to use
Serif
Sans Serif
Script

Requirements
Must have
• Designers,
• we really like the design of ameliadrovenko.com(we have attached a picture of the website) , Can we get a homepage like that? so the designs you submit will be 3 pages. The first one should be a page that only has Shop/Look. then the shop page, it should be nothing but our product which we will list the categories ourself. And the look page should contain all the info. such as news, about us and designers etc. Thank you all for your hard work, we really enjoyed the designs.

```html
<!DOCTYPE html>
<html lang="en">
<head>
<meta charset="utf-8">
<title>The Bright Quarry</title>
<link rel="stylesheet" href="https://fonts.googleapis.com/css2?family=Lora:wght@400&family=Raleway:wght@400;500&display=swap">
<style>
  :root {
    --sidebar-bg: #ffffff;
    --ink: #2b2b2b;
    --muted: #555555;
    --accent: #b3231f;
    --white: #ffffff;
    --rule: rgba(255,255,255,0.75);
    --stage-dark: #1c141c;
    --stage-mid: #4a3a4c;
    --stage-light: #cdb7cf;
    --spinner: #d8b84a;
  }
  * { box-sizing: border-box; margin: 0; padding: 0; }
  html, body { width: 1200px; height: 675px; overflow: hidden; }
  body { position: relative; font-family: "Raleway", sans-serif; background: var(--stage-dark); }

  .sidebar {
    position: absolute; left: 0; top: 0; width: 148px; height: 675px;
    background: var(--sidebar-bg); text-align: center; z-index: 2;
  }
  .brand { position: absolute; top: 22px; left: 0; width: 148px; }
  .brand-mark { width: 38px; height: 38px; border-radius: 50%; background: var(--accent); margin: 0 auto 8px; }
  .brand-name {
    font-family: "Lora", serif; font-size: 9.5px; line-height: 9px; letter-spacing: 0.8px;
    color: var(--ink); text-transform: uppercase;
  }
  .main-nav { position: absolute; top: 114px; left: 0; width: 148px; list-style: none; }
  .main-nav li { height: 25px; font-size: 10px; color: var(--ink); }
  .main-nav li.shop-link { color: var(--accent); }
  .sidebar-prev { position: absolute; left: 68px; top: 331px; }
  .sidebar-social { position: absolute; top: 606px; left: 0; width: 148px; display: flex; justify-content: center; gap: 12px; }
  .social-dot { width: 7px; height: 7px; border-radius: 50%; background: var(--muted); }
  .copyright { position: absolute; top: 632px; left: 0; width: 148px; font-size: 7px; line-height: 11px; color: var(--ink); }

  .stage {
    position: absolute; left: 148px; top: 0; width: 1052px; height: 675px;
    background:
      radial-gradient(ellipse 260px 420px at 300px 300px, rgba(210,185,215,0.55), transparent 70%),
      radial-gradient(ellipse 380px 200px at 420px 640px, rgba(235,225,238,0.7), transparent 70%),
      linear-gradient(90deg, #2a1f2c 0%, var(--stage-mid) 30%, #5d4c60 45%, #2e2430 70%, var(--stage-dark) 100%);
  }

  .cart { position: absolute; right: 46px; top: 14px; display: flex; align-items: center; gap: 9px; color: var(--white); font-size: 9px; }

  .hero-title {
    position: absolute; left: 188px; top: 255px; font-family: "Lora", serif; font-weight: 400;
    font-size: 36px; color: var(--white); letter-spacing: 0.2px; z-index: 1;
  }
  .share { position: absolute; right: 46px; top: 278px; display: flex; align-items: center; gap: 11px; color: var(--white); font-size: 9px; z-index: 1; }
  .share .social-dot { background: var(--white); }
  .rule { position: absolute; left: 188px; width: 966px; height: 1px; background: var(--rule); z-index: 1; }
  .rule-top { top: 309px; }
  .rule-bottom { top: 561px; }
  .hero-text { position: absolute; left: 188px; top: 322px; width: 300px; font-size: 9px; line-height: 17px; color: var(--white); z-index: 1; }
  .gallery-nav { position: absolute; left: 1126px; top: 334px; display: flex; gap: 12px; z-index: 1; }

  .look-gallery { position: absolute; left: 188px; top: 380px; display: flex; gap: 15px; z-index: 1; }
  .look { width: 125px; height: 156px; }
  .look-1 { background: linear-gradient(160deg, #1d2c55, #4d6aa8 60%, #20315a); }
  .look-2 { background: linear-gradient(160deg, #c9c9c9, #6f6f6f 60%, #2a2a2a); }
  .look-3 { background: linear-gradient(180deg, #e4e4e4, #3a3a3e 55%, #2a2a2e); }
  .look-4 { background: linear-gradient(160deg, #1a1d30, #6a5a74 55%, #a76a58); }
  .look-5 { background: linear-gradient(180deg, #f0eeee, #4a2e36 50%, #2d1e24); }
  .look-6 { background: linear-gradient(180deg, #e9ebeb, #d4d7d8 60%, #b9bdbe); }
  .look-7 { background: linear-gradient(180deg, #b9daf0, #3c7fbf 60%, #1d4f8a); }

  .shop-button {
    position: absolute; left: 1065px; top: 590px; width: 89px; height: 25px;
    background: var(--accent); color: var(--white); font-size: 11.5px; letter-spacing: 0.2px;
    display: flex; align-items: center; justify-content: center; z-index: 1;
  }
  .loader { position: absolute; left: 562px; top: 637px; z-index: 1; }
</style>
</head>
<body>
  <aside class="sidebar">
    <div class="brand">
      <div class="brand-mark"></div>
      <div class="brand-name">QLV Group<br>The Bright Quarry</div>
    </div>
    <ul class="main-nav">
      <li>Home</li>
      <li>About</li>
      <li>Designer</li>
      <li>News</li>
      <li>Members Center</li>
      <li class="shop-link">Shop Now</li>
    </ul>
    <svg class="sidebar-prev" width="10" height="14" viewBox="0 0 10 14"><polyline points="8,1 2,7 8,13" fill="none" stroke="#777" stroke-width="1.3"/></svg>
    <div class="sidebar-social">
      <span class="social-dot"></span><span class="social-dot"></span><span class="social-dot"></span><span class="social-dot"></span>
    </div>
    <p class="copyright">Copyright @ 2014 &nbsp;The Bright Quarry<br>All rights reserved.</p>
  </aside>

  <main class="stage" role="img" aria-label="Runway show photograph with models walking under purple light"></main>

  <div class="cart">
    <svg width="11" height="13" viewBox="0 0 11 13"><rect x="1" y="4" width="9" height="8.5" fill="none" stroke="#fff" stroke-width="1.2"/><path d="M3.5 4V2.8a2 2 0 0 1 4 0V4" fill="none" stroke="#fff" stroke-width="1.2"/></svg>
    <span>3</span>
  </div>

  <h1 class="hero-title">The Bright Quarry</h1>
  <div class="share"><span>Share:</span><span class="social-dot"></span><span class="social-dot"></span><span class="social-dot"></span><span class="social-dot"></span></div>
  <div class="rule rule-top"></div>
  <p class="hero-text">A hand shop to buy the product in the form of collection of designer fashion stores as well as personal customization combined boutiques.</p>
  <div class="gallery-nav">
    <svg width="7" height="11" viewBox="0 0 7 11"><polyline points="6,1 1.5,5.5 6,10" fill="none" stroke="#fff" stroke-width="1.4"/></svg>
    <svg width="7" height="11" viewBox="0 0 7 11"><polyline points="1,1 5.5,5.5 1,10" fill="none" stroke="#fff" stroke-width="1.4"/></svg>
  </div>

  <div class="look-gallery">
    <div class="look look-1" role="img" aria-label="Look photo: model in blue printed dress"></div>
    <div class="look look-2" role="img" aria-label="Look photo: black and white backless dress"></div>
    <div class="look look-3" role="img" aria-label="Look photo: man in dark suit"></div>
    <div class="look look-4" role="img" aria-label="Look photo: model in multicolour print dress"></div>
    <div class="look look-5" role="img" aria-label="Look photo: man in dark printed shirt"></div>
    <div class="look look-6" role="img" aria-label="Look photo: model in white cropped jacket"></div>
    <div class="look look-7" role="img" aria-label="Look photo: model in blue print dress"></div>
  </div>
  <div class="rule rule-bottom"></div>

  <div class="shop-button">SHOP NOW</div>
  <svg class="loader" width="26" height="14" viewBox="0 0 26 14"><path d="M2 13 A11 11 0 0 1 24 13" fill="none" stroke="var(--spinner)" stroke-width="2"/></svg>
</body>
</html>
```